Business Card for a recruitment agency specializing in engineers and geeks.

I am looking to create Business Card Design for my company.
That
## Company name:
Quorvant Inc.
Quorvant is a term coined from the following concepts.
1. geek + engineer
2. geek utopia
## Company Description:
The concept of the company is to be a recruitment agency that creates a paradise for geeky engineers. We want to be a place where engineers can have more freedom and ideal career support.
# Target.
The noun itself is often given to companies that want to hire engineers, geeks, and IT-related personnel, so it would be nice to get the impression that this company seems to have good engineers and IT personnel. There are many occasions where I meet with the human resources department, president, or senior management and give it to them.
# Atmosphere
We are happy with simplicity, but with an impact that will help people remember the company. The logo is based on a dinosaur that does programming, so it should be somewhat playful, but since it will basically be used in a business setting, please don't make it too silly.
# About the logo
See the attached files. The company logo represents our engineers smiling upward because of our work, with the motif of a dinosaur doing programming.
## Color
We will leave the color scheme to you, but since the logo is in black and white, colors with such a taste would fit well.
## file format
ai, psd, png, svg
Industry/Entity Type
human resource and employment agency
Contact Information for Business Card
Company name, address, email, tel, URL,logo
Colors
Designer to choose colors to be used in the design.

```html
<!DOCTYPE html>
<html lang="en">
<head>
<meta charset="utf-8">
<title>Quorvant Inc. — Business Card</title>
<link rel="stylesheet" href="https://fonts.googleapis.com/css2?family=Arimo:wght@400;500;700&display=swap">
<style>
  :root {
    --backdrop: #2b2b2d;
    --card: #0b0b0c;
    --accent: #1ea7ec;
    --ink: #f2f2f2;
    --rule: #4a4a4a;
  }
  * { box-sizing: border-box; margin: 0; padding: 0; }
  html, body {
    width: 1200px; height: 900px; overflow: hidden;
    background: var(--backdrop);
    font-family: "Arimo", Arial, sans-serif;
  }
  .canvas {
    width: 1200px; height: 900px;
    display: flex; align-items: center; justify-content: center; gap: 40px;
  }
  .card {
    width: 560px; height: 320px;
    background: var(--card);
    position: relative;
    box-shadow: 0 10px 30px rgba(0,0,0,.45);
  }
  /* front */
  .brand-block {
    position: absolute; left: 0; top: 0; width: 250px; height: 100%;
    display: flex; flex-direction: column; align-items: center; justify-content: center; gap: 18px;
  }
  .brand-square {
    width: 74px; height: 74px;
    border: 7px solid var(--accent);
    border-radius: 6px;
  }
  .brand-name {
    color: var(--accent);
    font-weight: 500;
    font-size: 40px;
    letter-spacing: 1px;
  }
  .divider {
    position: absolute; left: 262px; top: 70px; width: 1px; height: 180px;
    background: var(--rule);
  }
  .details {
    position: absolute; left: 290px; top: 68px; color: var(--ink);
  }
  .person-name {
    color: var(--accent); font-weight: 700; font-size: 20px; letter-spacing: .5px;
  }
  .person-role { font-size: 15px; margin-top: 2px; }
  .contact-list { list-style: none; margin-top: 16px; }
  .contact-list li {
    display: flex; align-items: center; gap: 9px;
    font-size: 15px; line-height: 22px;
  }
  .contact-list svg { width: 14px; height: 14px; flex: none; fill: none; stroke: var(--accent); stroke-width: 1.8; }
  .contact-list .highlight { color: var(--accent); }
  .address { font-size: 15px; line-height: 20px; margin-top: 14px; padding-left: 23px; }
  /* back */
  .card--back {
    display: flex; align-items: center; justify-content: center; gap: 20px;
  }
  .card--back .brand-square { width: 64px; height: 64px; border-width: 6px; }
</style>
</head>
<body>
<main class="canvas">
  <section class="card card--front" aria-label="Business card front">
    <div class="brand-block">
      <div class="brand-square" aria-hidden="true"></div>
      <div class="brand-name">Quorvant</div>
    </div>
    <div class="divider"></div>
    <div class="details">
      <p class="person-name">DANIEL HART</p>
      <p class="person-role">Managing Director</p>
      <ul class="contact-list">
        <li>
          <svg viewBox="0 0 16 16"><path d="M4 2l2.5 3-1.5 1.5c.8 2 2.5 3.7 4.5 4.5L11 9.5l3 2.5-1.5 2C7.5 14 2 8.5 2 3.5z"/></svg>
          044-555 210 384
        </li>
        <li>
          <svg viewBox="0 0 16 16"><rect x="1.5" y="3.5" width="13" height="9"/><path d="M1.5 3.5L8 9l6.5-5.5"/></svg>
          info@quorvant.com
        </li>
        <li>
          <svg viewBox="0 0 16 16"><circle cx="8" cy="8" r="6.5"/><path d="M1.5 8h13M8 1.5c-3 3.5-3 9.5 0 13M8 1.5c3 3.5 3 9.5 0 13"/></svg>
          <span>www.<span class="highlight">quorvant</span>.com</span>
        </li>
      </ul>
      <p class="address">118 Harbor Lane, Suite 4<br>45210, Northland</p>
    </div>
  </section>

  <section class="card card--back" aria-label="Business card back">
    <div class="brand-square" aria-hidden="true"></div>
    <div class="brand-name">Quorvant</div>
  </section>
</main>
</body>
</html>
```